Tess Marlowe Communication business card

I am starting a small, country-based business that offers writing, communication and marketing services to a wide range of clients, inner city big business, to mining, through to agriculture.

The appeal of my business is that it's mobile and flexible. It's just me, with lots of hands-on experience on construction and infrastructure projects.

I can provide the following services:

• Communication planning and management
• Issues and media management
• Marketing and communication materials
• Project management and strategy
• Government liaison
• Incident management communication
• Stakeholder management

It would be great to be able to use the elements of the business card design on other stationery.

Industry/Entity Type

Communication

Requirements
Must have
• The following information:

Tess Marlowe
M: 0427 391 864
E: tess@tmcommsmail.com

PO Box 152
Durrandale Q 4472
Nice to have
• a rural element (windmill, workboots, wheat stalk)

```html
<!DOCTYPE html>
<html lang="en">
<head>
<meta charset="utf-8">
<title>Tess Marlowe Communication – Stationery</title>
<link rel="stylesheet" href="https://fonts.googleapis.com/css2?family=Exo+2:wght@300;400;700&display=swap">
<style>
  :root {
    --bg-light: #eef0ef;
    --bg-dark: #9a9c9c;
    --paper: #ffffff;
    --ink: #25292c;
    --ink-soft: #3a3f42;
    --brand-green: #6aa542;
    --leaf-green: #7cb85a;
    --mist-green: #cdebc6;
    --faint-green: #d6efd0;
    --shadow: 3px 4px 6px rgba(0,0,0,0.45);
  }
  * { box-sizing: border-box; margin: 0; padding: 0; }
  html, body { width: 1200px; height: 900px; overflow: hidden; }
  body {
    position: relative;
    font-family: "Exo 2", sans-serif;
    background: radial-gradient(ellipse at 45% 40%, var(--bg-light) 0%, #dfe1e0 45%, var(--bg-dark) 100%);
  }
  .sheet { position: absolute; background: var(--paper); box-shadow: var(--shadow); overflow: hidden; }

  /* Business card front */
  .card-front { left: 46px; top: 100px; width: 487px; height: 314px; }
  .card-front .flower {
    position: absolute; left: 312px; top: 10px; width: 175px; height: 245px;
    background: radial-gradient(ellipse at 50% 35%, var(--leaf-green) 0%, rgba(124,184,90,0.55) 55%, rgba(124,184,90,0) 75%);
  }
  .wordmark { position: absolute; text-align: right; color: var(--ink); }
  .wordmark .name { display: block; font-weight: 700; letter-spacing: 0.5px; line-height: 1; }
  .wordmark .tag { display: block; font-weight: 300; color: var(--ink-soft); line-height: 1; }
  .card-front .wordmark { left: 38px; top: 58px; width: 246px; }
  .card-front .wordmark .name { font-size: 39px; }
  .card-front .wordmark .tag { font-size: 25px; margin-top: 2px; }
  .card-front .holder { position: absolute; left: 41px; top: 196px; font-size: 22px; color: var(--brand-green); }
  .card-front .contact { position: absolute; left: 41px; top: 232px; font-size: 18px; line-height: 25px; color: var(--ink); }
  .sep { display: inline-block; width: 4px; height: 4px; background: var(--brand-green); vertical-align: middle; margin: 0 6px; }

  /* Business card back */
  .card-back {
    left: 286px; top: 391px; width: 494px; height: 320px;
    background: var(--brand-green); color: #fff;
    display: flex; flex-direction: column; align-items: center; padding-top: 68px;
  }
  .services { list-style: none; text-align: center; font-size: 18px; line-height: 39px; }

  .label { position: absolute; font-family: Arial, sans-serif; font-size: 22px; color: #111; }
  .label-front { left: 42px; top: 427px; }
  .label-back { left: 290px; top: 724px; }

  /* Letterhead */
  .letterhead { left: 581px; top: 52px; width: 559px; height: 791px; }
  .letterhead .flower {
    position: absolute; left: 389px; top: 0; width: 170px; height: 245px;
    background: radial-gradient(ellipse at 50% 30%, var(--faint-green) 0%, rgba(214,239,208,0.6) 55%, rgba(214,239,208,0) 78%);
  }
  .letterhead .wordmark { right: 60px; top: 46px; width: 300px; }
  .letterhead .wordmark .name { font-size: 44px; }
  .letterhead .wordmark .tag { font-size: 28px; margin-top: 2px; }
  .letterhead .footer-band {
    position: absolute; left: 0; bottom: 0; width: 100%; height: 56px;
    background: var(--mist-green);
    display: flex; align-items: center; justify-content: center;
    font-size: 13px; color: #555; gap: 10px;
  }
  .footer-band b { color: var(--ink); font-weight: 700; }
  .footer-band .dot { width: 3px; height: 3px; border-radius: 50%; background: #fff; }
</style>
</head>
<body>

  <section class="sheet card-front">
    <div class="flower" role="img" aria-label="Green illustration of a flowering wild plant on a tall stem"></div>
    <div class="wordmark">
      <span class="name">Tess Marlowe</span>
      <span class="tag">Communication</span>
    </div>
    <p class="holder">Tess Marlowe</p>
    <p class="contact">
      M: 0427 391 864<span class="sep"></span>E: tess@tmcommsmail.com<br>
      PO Box 152<span class="sep"></span>Durrandale Q 4472
    </p>
  </section>
  <p class="label label-front">Front</p>

  <section class="sheet letterhead">
    <div class="flower" role="img" aria-label="Faint green illustration of a flowering wild plant"></div>
    <div class="wordmark">
      <span class="name">Tess Marlowe</span>
      <span class="tag">Communication</span>
    </div>
    <footer class="footer-band">
      <span><b>M:</b> 0427 391 864</span><span class="dot"></span>
      <span><b>E:</b> tess@tmcommsmail.com</span><span class="dot"></span>
      <span>PO Box 152</span><span class="dot"></span>
      <span>Durrandale Q 4472</span>
    </footer>
  </section>

  <section class="sheet card-back">
    <ul class="services">
      <li>Stakeholder engagement</li>
      <li>Issues and media management</li>
      <li>Development of communication material</li>
      <li>Government liaison</li>
      <li>Facilitation</li>
    </ul>
  </section>
  <p class="label label-back">Back</p>

</body>
</html>
```